Business Card Design for a Private Label Pet Company

We need a business card design for our family-owned company, Hollow Creek Pet Works (www.hollowcreekpetworks.com), out of St. Louis, MO. We provide turnkey private label solutions for retailers, Marketvale sellers and other brands who want to provide high quality, natural, Made in the USA pet products to their customers. Our customer are worldwide and range from the US to the UK to Vietnam and beyond. We offer private label for dozens of pet products including grooming products (shampoos, conditioners, colognes, ear and eye washes, mouthwash, etc.), all meat treats, supplements, and specialty products (pet stain and odor cleaner, anti-chew spray, etc.). We would like to see designs that use the colors, fonts and logos (see variations) within our brand guidelines and fit with the look and feel from our website.

Target Market(s)

Pet Store Owners, Marketvale Sellers, Pet Brand Marketers

Industry/Entity Type

Pet

Contact Information for Business Card

Tom Willoughby
CEO
Hollow Creek Pet Works
5817 Brookhaven Commerce Lane
St. Louis, MO 63521
office: 314.555.0182
mobile: 770.555.0139
email: tom@hollowcreekpetworks.com

Colors

Designer to choose colors to be used in the design.

Requirements
Must have
• Need to follow the brand guidelines attached for colors, fonts and logos
• Need to use the logos attached (or a variation) with our without the tagline
• Name, title, phone (office and mobil), email, address on the business card
• Clean professional look and feel that says: high quality natural pet products, high quality service, made in the USA
Nice to have
• Made in the USA is a big positive in our industry and we are very proud of it. There is an attached icon from our website. The designer can get creative here as they wish.
• I do like using color for pop. Just don't like lots of bright, loud colors.
Should not have
• lots of bright, loud colors
• overwhelming to the reader
• crowded

```html
<!DOCTYPE html>
<html lang="en">
<head>
<meta charset="utf-8">
<title>Hollow Creek Pet Works – Business Card</title>
<link rel="stylesheet" href="https://fonts.googleapis.com/css2?family=Montserrat:ital,wght@0,400;0,700;0,800;1,600&display=swap">
<style>
  :root {
    --olive: #8a9a5b;
    --olive-dark: #7d8c4f;
    --paper: #ffffff;
    --backdrop: #eeeeee;
    --shadow: rgba(0, 0, 0, 0.12);
  }
  * { box-sizing: border-box; margin: 0; padding: 0; }
  html, body {
    width: 1200px; height: 800px; overflow: hidden;
    background: var(--backdrop);
    font-family: "Montserrat", sans-serif;
  }
  .canvas {
    width: 1200px; height: 800px;
    display: flex; align-items: center; justify-content: center; gap: 60px;
  }
  .card {
    width: 525px; height: 300px;
    border-radius: 3px;
    box-shadow: 0 10px 28px var(--shadow);
    position: relative; overflow: hidden;
  }

  /* Front */
  .card-front {
    background: var(--olive);
    display: flex; flex-direction: column; align-items: center; justify-content: center;
    color: var(--paper);
  }
  .brand-name {
    font-weight: 800; font-size: 34px; letter-spacing: 0.5px;
    text-transform: uppercase; text-align: center; line-height: 1.1;
  }
  .brand-rule {
    width: 360px; height: 2px; background: var(--paper); opacity: 0.85;
    margin-top: 22px;
  }

  /* Back */
  .card-back {
    background: var(--paper);
    display: flex; padding: 46px 34px 40px 40px;
    color: var(--olive-dark);
  }
  .card-back::after {
    content: ""; position: absolute; left: 0; right: 0; bottom: 0;
    height: 12px; background: var(--olive);
  }
  .person {
    width: 180px; text-align: right; padding-right: 20px; padding-top: 4px;
  }
  .person-name { font-weight: 800; font-size: 19px; }
  .person-title { font-style: italic; font-weight: 600; font-size: 10px; margin-top: 5px; }
  .divider {
    width: 2px; background: var(--olive); align-self: stretch; margin-bottom: 10px;
  }
  .contact { padding-left: 20px; padding-top: 48px; font-size: 11.5px; }
  .company-name { font-weight: 700; font-size: 12.5px; margin-bottom: 9px; }
  .contact-row { display: flex; align-items: flex-start; gap: 8px; margin-bottom: 6px; line-height: 1.35; }
  .contact-row svg { width: 11px; height: 11px; flex: none; margin-top: 2px; fill: none; stroke: var(--olive-dark); stroke-width: 1.6; }
  .contact-row svg.solid { fill: var(--olive-dark); stroke: none; }
</style>
</head>
<body>
<main class="canvas">
  <section class="card card-front" aria-label="Card front">
    <h1 class="brand-name">Hollow Creek Pet Works</h1>
    <div class="brand-rule"></div>
  </section>

  <section class="card card-back" aria-label="Card back">
    <div class="person">
      <p class="person-name">Tom Willoughby</p>
      <p class="person-title">Chief Executive Officer</p>
    </div>
    <div class="divider"></div>
    <div class="contact">
      <p class="company-name">Hollow Creek Pet Works</p>
      <div class="contact-row">
        <svg class="solid" viewBox="0 0 12 12" aria-hidden="true"><path d="M6 0.5a4 4 0 0 0-4 4c0 3 4 7 4 7s4-4 4-7a4 4 0 0 0-4-4zm0 5.6a1.6 1.6 0 1 1 0-3.2 1.6 1.6 0 0 1 0 3.2z"/></svg>
        <span>5817 Brookhaven Commerce Lane<br>St. Louis MO 63521</span>
      </div>
      <div class="contact-row">
        <svg class="solid" viewBox="0 0 12 12" aria-hidden="true"><path d="M2.4 0.8l1.8-.3 1.1 2.6-1.2.9a6.5 6.5 0 0 0 3 3l.9-1.2 2.6 1.1-.3 1.8c-.1.5-.6.9-1.1.9C5 9.6 1.6 6.2 1.5 1.9c0-.5.4-1 .9-1.1z"/></svg>
        <span>314.555.0182</span>
      </div>
      <div class="contact-row">
        <svg viewBox="0 0 12 12" aria-hidden="true"><rect x="3" y="0.8" width="6" height="10.4" rx="1"/></svg>
        <span>770.555.0139</span>
      </div>
      <div class="contact-row">
        <svg viewBox="0 0 12 12" aria-hidden="true"><rect x="0.8" y="2.2" width="10.4" height="7.6" rx="0.8"/><path d="M1 2.6l5 4 5-4"/></svg>
        <span>tom@hollowcreekpetworks.com</span>
      </div>
    </div>
  </section>
</main>
</body>
</html>
```